Hour of Harvest Podcast Graphic

Need a catchy graphic that displays with a podcast post on Facebook. I want this graphic to post with each podcast. It won't be a logo but a familiar design identifying the podcast.

Target Market(s)

People with money to invest and concerned about taxes

Font styles to use
Sans Serif

Colors
886aae
b768aa
33b8a4
fec214

Requirements
Must have
• My name, such as "Hour of Harvest w/Ned Pruett" laid out cool. (take creative control)
• Want to portray a Biblical/Christian worldview. Will discuss Taxes and Investments and bible verses. Want it to be noticed on Facebook.
Nice to have
• My photo to be visible but like a watermark if you can at least see my face. Black and white my photo but the text can be colorful and graphics can be added.
Should not have
• Not to busy

```html
<!DOCTYPE html>
<html lang="en">
<head>
<meta charset="utf-8">
<title>Hour of Harvest w/Ned Pruett</title>
<link rel="stylesheet" href="https://fonts.googleapis.com/css2?family=Oswald:wght@500&display=swap">
<style>
  :root {
    --gold: #fec214;
    --teal: #33b8a4;
    --storm-dark: #1c2530;
    --storm-mid: #3a4550;
    --cloud: #b9b4ab;
    --brush: #f4f4f2;
    --photo-dark: #2a2624;
    --photo-mid: #6e5f55;
  }
  html, body {
    margin: 0;
    padding: 0;
    overflow: hidden;
    background: var(--storm-dark);
  }
  .cover {
    position: relative;
    width: 1200px;
    height: 1200px;
    overflow: hidden;
    background:
      radial-gradient(ellipse 420px 300px at 420px 380px, rgba(200,195,185,0.55), transparent 70%),
      radial-gradient(ellipse 380px 260px at 220px 1000px, rgba(170,165,155,0.45), transparent 70%),
      radial-gradient(ellipse 300px 220px at 120px 560px, rgba(150,148,140,0.35), transparent 70%),
      linear-gradient(160deg, var(--storm-dark) 0%, var(--storm-mid) 55%, #4a4a48 100%);
  }
  .cloud-scene {
    position: absolute;
    inset: 0;
  }
  .host-portrait {
    position: absolute;
    top: 0;
    right: 0;
    width: 560px;
    height: 1200px;
    background:
      radial-gradient(ellipse 210px 280px at 340px 430px, #a88a72 0%, #7a6252 55%, transparent 80%),
      linear-gradient(180deg, #5a4f48 0%, var(--photo-mid) 40%, var(--photo-dark) 75%, #1e2230 100%);
    -webkit-mask-image: linear-gradient(90deg, transparent 0%, #000 22%);
    mask-image: linear-gradient(90deg, transparent 0%, #000 22%);
  }
  .frame {
    position: absolute;
    inset: 0;
  }
  .title {
    position: absolute;
    left: 62px;
    top: 360px;
    margin: 0;
    font-family: "Oswald", sans-serif;
    font-weight: 500;
    color: var(--gold);
    text-transform: uppercase;
    line-height: 0.78;
    font-size: 250px;
    letter-spacing: 2px;
  }
  .title-line {
    display: block;
    height: 198px;
  }
  .title-line--long {
    font-size: 218px;
  }
  .host-tag {
    position: absolute;
    left: 305px;
    top: 605px;
    width: 520px;
    height: 170px;
    transform: rotate(-6deg);
  }
  .host-tag svg {
    position: absolute;
    inset: 0;
  }
  .host-name {
    position: absolute;
    left: 70px;
    top: 42px;
    font-family: "Oswald", sans-serif;
    font-weight: 500;
    font-size: 56px;
    color: var(--teal);
    text-transform: uppercase;
    letter-spacing: 1px;
    white-space: nowrap;
  }
  .host-name small {
    font-size: 44px;
    margin-right: 10px;
  }
</style>
</head>
<body>
  <main class="cover">
    <div class="cloud-scene" role="img" aria-label="Dramatic billowing clouds against a dark stormy sky"></div>
    <div class="host-portrait" role="img" aria-label="Portrait of host Ned Pruett in a dark suit and patterned tie, smiling"></div>

    <svg class="frame" width="1200" height="1200" viewBox="0 0 1200 1200" aria-hidden="true">
      <g stroke="var(--gold)" stroke-width="5" fill="none">
        <line x1="48" y1="50" x2="740" y2="50"/>
        <line x1="50" y1="48" x2="50" y2="1152"/>
        <line x1="48" y1="1150" x2="1152" y2="1150"/>
        <line x1="1150" y1="560" x2="1150" y2="1152"/>
      </g>
    </svg>

    <h1 class="title">
      <span class="title-line">Hour</span>
      <span class="title-line">Of</span>
      <span class="title-line title-line--long">Harvest</span>
    </h1>

    <div class="host-tag">
      <svg viewBox="0 0 520 170" width="520" height="170" aria-hidden="true">
        <path fill="var(--brush)" d="M30 40 C120 28 300 22 505 30 L498 50 L515 62 L500 78 L512 96 L490 110 C330 118 170 128 20 150 L40 132 L8 118 L34 104 L12 88 L40 74 L14 58 Z"/>
      </svg>
      <span class="host-name"><small>w/</small>Ned Pruett</span>
    </div>
  </main>
</body>
</html>
```